Troven Wine Label Design Project

We are creating a wine with a winery in New Hampshire. USA. The bottles need a label Here are some specifics
Brand name Lumen XIV (latin for Light 14)
Wine: is a blend of Cabernet Sauvignon, Merlot and Shiraz (dominant varietal is cabernet)
Vintage 2023
All ideas from here are thoughts:
Elegant serif or calligraphic script for a sophisticated look. Perhaps Gold foil or embossed for prominence.
Background suggestions: deep Burgandy or matt black for contrast
Illustrations suggestions: Roman inspired wreath (laurel) or column or stylized roman coin.
Tagline suggestion: Timeless
All these graphic elements are just suggestions, you all are the pros. have at it and good luck

```html
<!DOCTYPE html>
<html lang="en">
<head>
<meta charset="UTF-8">
<title>Lumen XIV — Wine Label</title>
<link rel="stylesheet" href="https://fonts.googleapis.com/css2?family=Oswald:wght@500&family=Cormorant+Garamond:wght@600;700&display=swap">
<style>
  :root {
    --backdrop: #38383b;
    --burgundy: #521726;
    --burgundy-deep: #3a0f1a;
    --gold: #c49a62;
    --gold-light: #e0bc86;
    --gold-dark: #8a6538;
    --ink: #4a1522;
  }
  * { margin: 0; padding: 0; box-sizing: border-box; }
  html, body { width: 1200px; height: 900px; overflow: hidden; background: var(--backdrop); }
  .canvas { position: relative; width: 1200px; height: 900px; background: var(--backdrop); }

  .label {
    position: absolute; left: 330px; top: 30px; width: 540px; height: 840px;
    background: linear-gradient(90deg, var(--burgundy-deep) 0%, var(--burgundy) 30%, var(--burgundy) 70%, var(--burgundy-deep) 100%);
  }
  .label-frame-outer {
    position: absolute; inset: 14px; border: 1.5px solid var(--gold);
  }
  .label-frame-inner {
    position: absolute; inset: 24px; border: 1px solid var(--gold-dark);
  }
  .corner-flourish {
    position: absolute; width: 54px; height: 54px;
    background: radial-gradient(circle at center, rgba(196,154,98,0.55), rgba(196,154,98,0) 70%);
  }
  .corner-flourish.tl { left: 18px; top: 18px; }
  .corner-flourish.tr { right: 18px; top: 18px; }
  .corner-flourish.bl { left: 18px; bottom: 18px; }
  .corner-flourish.br { right: 18px; bottom: 18px; }

  .title-box {
    position: absolute; left: 70px; top: 90px; width: 400px; height: 116px;
    border: 2px solid var(--gold); border-radius: 14px;
    display: flex; align-items: center; justify-content: center;
  }
  .title-box::before {
    content: ""; position: absolute; inset: -9px; border: 1px solid var(--gold-dark); border-radius: 20px;
  }
  .brand-name {
    font-family: "Oswald", sans-serif; font-weight: 500; font-size: 56px;
    letter-spacing: 8px; line-height: 1; color: var(--gold-light);
  }

  .divider { position: absolute; left: 0; width: 540px; height: 40px; }
  .divider.upper { top: 220px; }
  .divider.lower { top: 540px; transform: scaleY(-1); }

  .medallion {
    position: absolute; left: 120px; top: 255px; width: 300px; height: 300px; border-radius: 50%;
    border: 3px solid var(--gold);
    background: radial-gradient(circle, var(--gold-dark) 0%, var(--gold) 60%, var(--gold-dark) 100%);
    display: flex; align-items: center; justify-content: center;
  }
  .medallion-portrait {
    width: 200px; height: 200px; border-radius: 50%; border: 2px solid var(--gold-light);
    background: radial-gradient(circle at 40% 35%, #c9a478, #9c7548);
  }

  .varietal-box {
    position: absolute; left: 70px; top: 595px; width: 400px; height: 110px;
    border: 2px solid var(--gold); border-radius: 12px; padding: 8px;
  }
  .varietal-plate {
    width: 100%; height: 100%; border-radius: 8px;
    background: linear-gradient(90deg, var(--gold-dark), var(--gold) 45%, var(--gold-light) 60%, var(--gold-dark));
    display: flex; flex-direction: column; align-items: center; justify-content: center;
    font-family: "Cormorant Garamond", serif; font-weight: 700; font-size: 25px;
    letter-spacing: 3px; line-height: 1.15; color: var(--ink);
  }

  .vintage, .origin {
    position: absolute; left: 0; width: 100%; text-align: center;
    font-family: "Cormorant Garamond", serif; font-weight: 600; color: var(--gold);
    font-variant-numeric: lining-nums; line-height: 1;
  }
  .vintage { top: 732px; font-size: 21px; letter-spacing: 4px; }
  .origin { top: 774px; font-size: 21px; letter-spacing: 5px; }
</style>
</head>
<body>
<main class="canvas">
  <section class="label">
    <div class="label-frame-outer"></div>
    <div class="label-frame-inner"></div>
    <div class="corner-flourish tl" role="img" aria-label="Gold ornamental corner flourish"></div>
    <div class="corner-flourish tr" role="img" aria-label="Gold ornamental corner flourish"></div>
    <div class="corner-flourish bl" role="img" aria-label="Gold ornamental corner flourish"></div>
    <div class="corner-flourish br" role="img" aria-label="Gold ornamental corner flourish"></div>

    <header class="title-box">
      <h1 class="brand-name">LUMEN XIV</h1>
    </header>

    <svg class="divider upper" viewBox="0 0 540 40">
      <path d="M70 8 Q270 40 470 8" fill="none" stroke="#c49a62" stroke-width="1.5"/>
    </svg>

    <div class="medallion">
      <div class="medallion-portrait" role="img" aria-label="Gold coin-style medallion with an engraved classical portrait, ringed by a key-pattern border"></div>
    </div>

    <svg class="divider lower" viewBox="0 0 540 40">
      <path d="M70 8 Q270 40 470 8" fill="none" stroke="#c49a62" stroke-width="1.5"/>
    </svg>

    <div class="varietal-box">
      <div class="varietal-plate">
        <span>CABERNET SAUVIGNON</span>
        <span>MERLOT • SHIRAZ</span>
      </div>
    </div>

    <p class="vintage">VINTAGE 2023</p>
    <p class="origin">NEW HAMPSHIRE. USA.</p>
  </section>
</main>
</body>
</html>
```